Construction Company Website

I need a website for my construction company
Target Market(s)
People looking for construction work
Coding
Coded - Design and coding required
Number of Pages Required
4 page
Colors
0455a3
ffc214
Requirements
Must have
- A home page about my company,
A completed projects page showcasing some completed works
A contact me page with an enquiry form
Nice to have
- Professional and contemporary whilst classy website.

```html
<!DOCTYPE html>
<html lang="en">
<head>
<meta charset="utf-8">
<title>Ridgeline Construction</title>
<link rel="stylesheet" href="https://fonts.googleapis.com/css2?family=Poppins:wght@400;500;600;700&family=Rubik:wght@400;500&display=swap">
<style>
  :root{
    --blue:#0455a3;
    --yellow:#ffc214;
    --ink:#1d1d1f;
    --text:#3b3b3b;
    --muted:#6b6b6b;
    --line:#c9c9c9;
    --navy:#1c2a48;
    --navy-deep:#17233d;
    --wood:#27221f;
    --white:#ffffff;
  }
  *{box-sizing:border-box;margin:0;padding:0}
  html,body{width:1200px;height:3893px;overflow:hidden;background:var(--white)}
  body{position:relative;font-family:"Rubik",sans-serif;color:var(--text)}
  .abs{position:absolute}

  /* header */
  .site-header{position:absolute;left:0;top:0;width:1200px;height:112px;background:var(--white);z-index:3}
  .brand-tab{position:absolute;left:58px;top:0;width:332px;height:170px;background:var(--white);border-radius:0 0 120px 120px / 0 0 70px 70px;z-index:4;text-align:center}
  .brand-mark{position:absolute;left:146px;top:14px;width:40px;height:40px;background:var(--yellow)}
  .brand-name{position:absolute;left:0;top:104px;width:332px;font-family:"Poppins",sans-serif;font-weight:500;font-size:24px;letter-spacing:4px;color:#d9a520}
  .brand-tagline{position:absolute;left:0;top:136px;width:332px;font-size:12px;color:#c9a54a;letter-spacing:.5px}
  .main-nav{position:absolute;top:50px;font-family:"Poppins",sans-serif;font-weight:500;font-size:15px;color:#2b2b2b}
  .main-nav.active{color:var(--yellow)}
  .nav-dot{position:absolute;left:571px;top:36px;width:9px;height:9px;border-radius:50%;background:var(--yellow)}
  .btn-contact{position:absolute;left:979px;top:38px;width:126px;height:41px;background:var(--blue);color:var(--white);font-family:"Poppins",sans-serif;font-weight:500;font-size:15px;display:flex;align-items:center;justify-content:center;border-radius:2px}

  /* hero */
  .hero{position:absolute;left:0;top:112px;width:1200px;height:670px}
  .hero-photo{position:absolute;inset:0;background:linear-gradient(180deg,#6f95c4 0%,#a9c3dc 20%,#3f6a3a 38%,#4d7a33 55%,#b9bcb0 68%,#5f9a2e 85%,#4b8a23 100%);clip-path:polygon(0 0,100% 0,100% 87%,50% 100%,0 87%)}
  .hero-edge{position:absolute;left:0;top:0;width:1200px;height:670px}
  .hero-title{position:absolute;left:0;width:1200px;text-align:center;font-family:"Poppins",sans-serif;font-weight:700;color:var(--white);text-shadow:0 2px 6px rgba(0,0,0,.35)}
  .hero-title.l1{top:300px;font-size:52px}
  .hero-title.l2{top:366px;font-size:42px}
  .hero-title .bar{display:inline-block;width:2px;height:36px;background:rgba(255,255,255,.7);margin:0 18px;vertical-align:-4px}
  .btn{position:absolute;display:flex;align-items:center;justify-content:center;font-family:"Poppins",sans-serif;font-weight:600;font-size:16px;color:var(--white)}
  .btn-blue{background:var(--blue)}
  .btn-yellow{background:var(--yellow)}
  .arrow-circle{position:absolute;width:48px;height:48px;border-radius:50%}

  /* about */
  .about{position:absolute;left:0;top:700px;width:1200px;height:674px;background:linear-gradient(180deg,#bcdcf3 0%,#e5f1fa 30%,#f3f8fb 58%,#dfe9df 74%,#d8e5b8 86%,#c7d89a 100%);z-index:0}
  .about-hills{position:absolute;left:0;top:1080px;width:1200px;height:294px;background:linear-gradient(180deg,rgba(170,190,210,.0) 0%,rgba(170,195,205,.5) 30%,rgba(196,214,150,.8) 60%,#c9da93 100%)}
  .about-title{position:absolute;left:0;width:1200px;text-align:center;font-family:"Poppins",sans-serif;font-weight:700}
  .about-title.main{top:880px;font-size:57px;color:var(--ink)}
  .about-title.sub{top:945px;font-size:40px;font-weight:500;color:var(--yellow)}
  .about-text{position:absolute;left:260px;width:680px;text-align:center;font-size:16px;line-height:30px;color:#3a3a3a}

  /* service tiles */
  .tile{position:absolute;top:1372px;height:376px}
  .tile-label{position:absolute;left:0;width:100%;top:252px;text-align:center;font-family:"Poppins",sans-serif;font-weight:600;font-size:23px;color:var(--white);text-shadow:0 1px 4px rgba(0,0,0,.5)}
  .tile-chevron{position:absolute;left:50%;top:303px;margin-left:-18px;width:36px;height:36px}

  /* services carousel */
  .svc-card{position:absolute;background:var(--white);border:2px solid #d4d4d4;text-align:center}
  .svc-card h3{position:absolute;left:0;width:100%;font-family:"Poppins",sans-serif;font-weight:600;font-size:18px;line-height:23px;color:#1e1e1e}
  .svc-card p{position:absolute;left:0;width:100%;font-size:15px;line-height:21px;color:#555}
  .svc-card.featured{background:var(--blue);border:none;box-shadow:0 16px 24px rgba(4,85,163,.28)}
  .svc-card.featured h3,.svc-card.featured p{color:var(--white)}
  .svc-icon{position:absolute;left:50%;margin-left:-34px;width:68px;height:68px}

  /* projects */
  .projects{position:absolute;left:0;top:2262px;width:1200px;height:787px;background:linear-gradient(90deg,#231f1d 0%,#2e2825 30%,#25201e 60%,#2c2623 100%)}
  .section-title{position:absolute;left:0;width:1200px;text-align:center;font-family:"Poppins",sans-serif;font-weight:700}
  .section-title .accent{color:var(--yellow)}
  .project{position:absolute}
  .view-more{background:linear-gradient(180deg,#1e4f8e 0%,#1f5aa3 100%);display:flex;flex-direction:column;align-items:center;justify-content:center}
  .view-more .vm-icon{width:38px;height:38px;border-radius:50%;background:var(--white);display:flex;align-items:center;justify-content:center;margin-bottom:18px}
  .view-more span{font-family:"Poppins",sans-serif;font-weight:600;font-size:27px;color:var(--white)}

  /* contact */
  .field{position:absolute;border:2px solid #c4c4c4;background:var(--white);font-size:17px;color:#5a5a5a;padding:11px 18px}
  .btn-outline{position:absolute;left:517px;top:3451px;width:166px;height:47px;border:2px solid var(--blue);border-radius:24px;display:flex;align-items:center;justify-content:center;font-family:"Poppins",sans-serif;font-weight:500;font-size:16px;color:#1e1e1e}

  /* footer */
  .site-footer{position:absolute;left:0;top:3571px;width:1200px;height:267px;background:var(--navy)}
  .footer-bar{position:absolute;left:0;top:3838px;width:1200px;height:55px;background:var(--navy-deep);border-top:1px solid #33466b;text-align:center;font-size:14px;line-height:55px;color:#c9cfdc}
  .foot-brand-mark{position:absolute;left:240px;top:3630px;width:60px;height:60px;background:var(--yellow)}
  .foot-brand-name{position:absolute;left:120px;top:3737px;width:300px;text-align:center;font-family:"Poppins",sans-serif;font-weight:500;font-size:23px;letter-spacing:4px;color:#d9a520}
  .foot-brand-tag{position:absolute;left:120px;top:3770px;width:300px;text-align:center;font-size:13px;color:#c9a54a}
  .foot-col h4{position:absolute;font-family:"Poppins",sans-serif;font-weight:600;font-size:20px;color:var(--yellow);top:3630px}
  .foot-link{position:absolute;font-size:14.5px;color:#d7dce6}
  .foot-icon{position:absolute;width:16px;height:16px}
</style>
</head>
<body>

<!-- header -->
<header class="site-header">
  <nav>
    <span class="nav-dot"></span>
    <span class="main-nav active" style="left:552px">HOME</span>
    <span class="main-nav" style="left:636px">ABOUT US</span>
    <span class="main-nav" style="left:754px">PROJECTS</span>
    <span class="main-nav" style="left:869px">SERVICES</span>
    <span class="btn-contact">CONTACT</span>
  </nav>
</header>
<div class="brand-tab">
  <span class="brand-mark"></span>
  <div class="brand-name">RIDGELINE</div>
  <div class="brand-tagline">Groundworks | Landscaping | Extensions</div>
</div>

<!-- hero -->
<section class="hero">
  <div class="hero-photo" role="img" aria-label="Photo of a newly laid patio and lawn beside a timber fenced play area under a blue sky"></div>
  <svg class="hero-edge" viewBox="0 0 1200 670">
    <polyline points="0,583 600,670 1200,583" fill="none" stroke="#ffc214" stroke-width="6"/>
  </svg>
  <div class="hero-title l1">Groundworks</div>
  <div class="hero-title l2">Landscaping<span class="bar"></span>Extensions</div>
  <span class="btn btn-blue" style="left:514px;top:447px;width:172px;height:51px">FREE ESTIMATES</span>
  <svg class="arrow-circle" style="left:106px;top:283px" viewBox="0 0 48 48">
    <circle cx="24" cy="24" r="22" fill="none" stroke="#fff" stroke-width="2.5"/>
    <polyline points="28,14 18,24 28,34" fill="none" stroke="#fff" stroke-width="2.5"/>
  </svg>
  <svg class="arrow-circle" style="left:1043px;top:283px" viewBox="0 0 48 48">
    <circle cx="24" cy="24" r="24" fill="#ffc214"/>
    <polyline points="20,14 30,24 20,34" fill="none" stroke="#fff" stroke-width="2.5"/>
  </svg>
</section>

<!-- about -->
<section class="about" role="img" aria-label="Soft illustrated backdrop of clouds, misty hills and green fields"></section>
<div class="about-hills"></div>
<h1 class="about-title main">ABOUT</h1>
<h2 class="about-title sub">CONSTRUCTION</h2>
<p class="about-text" style="top:1013px">Lorem Ipsum is simply dummy text of the printing and typesetting industry. Lorem Ipsum has been the industry's standard dummy text ever since the 1500s, when an unknown printer took a galley of type and scrambled it to make.</p>
<p class="about-text" style="top:1126px">Lorem Ipsum is simply dummy text of the printing and typesetting industry. Lorem Ipsum has been the industry's standard dummy text ever since</p>
<span class="btn btn-yellow" style="left:514px;top:1219px;width:172px;height:52px">FREE ESTIMATES</span>

<!-- service tiles -->
<div class="tile" style="left:0;width:391px;background:linear-gradient(180deg,#4f6a3c 0%,#7a5a3f 30%,#2e9fd9 45%,#8a6040 62%,#6e5038 100%)" role="img" aria-label="Photo of a swimming pool being installed in a garden">
  <div class="tile-label">GROUNDWORKS</div>
  <svg class="tile-chevron" viewBox="0 0 36 36"><circle cx="18" cy="18" r="16" fill="none" stroke="#fff" stroke-width="2"/><polyline points="11,15 18,22 25,15" fill="none" stroke="#fff" stroke-width="2"/></svg>
</div>
<div class="tile" style="left:400px;width:399px;background:linear-gradient(180deg,#4f7a2e 0%,#6a5a36 35%,#9b4a26 60%,#7d8a2f 100%)" role="img" aria-label="Photo of a red brick garden path beside a lawn">
  <div class="tile-label">LANDSCAPING</div>
  <svg class="tile-chevron" viewBox="0 0 36 36"><circle cx="18" cy="18" r="16" fill="none" stroke="#fff" stroke-width="2"/><polyline points="11,15 18,22 25,15" fill="none" stroke="#fff" stroke-width="2"/></svg>
</div>
<div class="tile" style="left:808px;width:392px;background:linear-gradient(180deg,#5f6f7c 0%,#7b8896 25%,#5f8a3e 50%,#c9c4b2 70%,#4f7d2c 100%)" role="img" aria-label="Photo of a house extension with a metal roof and climbing ivy">
  <div class="tile-label">EXTENSIONS</div>
  <svg class="tile-chevron" viewBox="0 0 36 36"><circle cx="18" cy="18" r="16" fill="none" stroke="#fff" stroke-width="2"/><polyline points="11,15 18,22 25,15" fill="none" stroke="#fff" stroke-width="2"/></svg>
</div>

<!-- services carousel -->
<svg class="abs" style="left:109px;top:1967px" width="48" height="48" viewBox="0 0 48 48"><circle cx="24" cy="24" r="22" fill="none" stroke="#555" stroke-width="2"/><polyline points="28,14 18,24 28,34" fill="none" stroke="#555" stroke-width="2"/></svg>
<svg class="abs" style="left:1043px;top:1967px" width="48" height="48" viewBox="0 0 48 48"><circle cx="24" cy="24" r="22" fill="none" stroke="#555" stroke-width="2"/><polyline points="20,14 30,24 20,34" fill="none" stroke="#555" stroke-width="2"/></svg>

<div class="svc-card" style="left:184px;top:1861px;width:257px;height:267px">
  <svg class="svc-icon" style="top:30px" viewBox="0 0 68 68" fill="none" stroke="#0455a3" stroke-width="2.5">
    <rect x="6" y="6" width="48" height="48"/>
    <line x1="6" y1="18" x2="54" y2="18"/><line x1="6" y1="30" x2="54" y2="30"/><line x1="6" y1="42" x2="54" y2="42"/>
    <line x1="22" y1="6" x2="22" y2="18"/><line x1="38" y1="6" x2="38" y2="18"/><line x1="14" y1="18" x2="14" y2="30"/><line x1="30" y1="18" x2="30" y2="30"/><line x1="46" y1="18" x2="46" y2="30"/><line x1="22" y1="30" x2="22" y2="42"/><line x1="38" y1="30" x2="38" y2="42"/>
  </svg>
  <h3 style="top:126px">GROUND<br>CONCRETE WORK</h3>
  <p style="top:189px">Lorem Ipsum is simply<br>dummy text of the printing</p>
</div>
<div class="svc-card featured" style="left:471px;top:1884px;width:257px;height:268px">
  <svg class="svc-icon" style="top:30px" viewBox="0 0 68 68" fill="none" stroke="#fff" stroke-width="2.5">
    <rect x="6" y="18" width="56" height="44"/>
    <circle cx="18" cy="18" r="8"/><circle cx="44" cy="14" r="5"/>
    <path d="M6 50 L24 36 L38 46 L62 28"/>
  </svg>
  <h3 style="top:126px">SOFT<br>LANDSCAPING</h3>
  <p style="top:189px">Lorem Ipsum is simply<br>dummy text of the printing</p>
</div>
<div class="svc-card" style="left:758px;top:1861px;width:257px;height:267px">
  <svg class="svc-icon" style="top:30px" viewBox="0 0 68 68" fill="none" stroke="#0455a3" stroke-width="2.5">
    <circle cx="40" cy="12" r="7"/>
    <rect x="4" y="24" width="60" height="38"/>
    <line x1="4" y1="36" x2="64" y2="36"/>
    <line x1="16" y1="62" x2="22" y2="36"/><line x1="30" y1="62" x2="32" y2="36"/><line x1="44" y1="62" x2="42" y2="36"/><line x1="56" y1="62" x2="52" y2="36"/>
  </svg>
  <h3 style="top:126px">HARD<br>LANDSCAPING</h3>
  <p style="top:189px">Lorem Ipsum is simply<br>dummy text of the printing</p>
</div>

<!-- projects -->
<section class="projects" role="img" aria-label="Dark wood grain backdrop"></section>
<h2 class="section-title" style="top:2341px;font-size:42px;color:var(--white)">COMPLETED <span class="accent">PROJECTS</span></h2>
<div class="project" style="left:178px;top:2436px;width:417px;height:246px;background:linear-gradient(180deg,#7b6a55 0%,#5a7a3a 40%,#5aa02a 70%,#4d8f24 100%)" role="img" aria-label="Photo of a fenced back garden with new artificial lawn"></div>
<div class="project" style="left:603px;top:2436px;width:418px;height:246px;background:linear-gradient(180deg,#a9412c 0%,#b8503a 45%,#dcdcd6 60%,#6d8a3a 80%,#5f7e30 100%)" role="img" aria-label="Photo of a brick house with a new white conservatory"></div>
<div class="project" style="left:178px;top:2691px;width:275px;height:246px;background:linear-gradient(180deg,#5a7040 0%,#7a5a3c 35%,#2aa0dc 55%,#8a6244 75%,#6f5038 100%)" role="img" aria-label="Photo of a garden swimming pool under construction"></div>
<div class="project view-more" style="left:461px;top:2691px;width:276px;height:246px">
  <div class="vm-icon">
    <svg width="16" height="16" viewBox="0 0 16 16" fill="none" stroke="#1f5aa3" stroke-width="1.8"><path d="M9 3h4v4"/><path d="M13 3L7 9"/><path d="M11 10v3H3V5h3"/></svg>
  </div>
  <span>View More</span>
</div>
<div class="project" style="left:745px;top:2691px;width:276px;height:246px;background:linear-gradient(180deg,#9ab4cf 0%,#a4553a 25%,#b0603e 60%,#c9bfa8 80%,#6f8c3c 100%)" role="img" aria-label="Photo of the rear of a brick house with a new paved patio"></div>

<!-- contact -->
<h2 class="section-title" style="top:3126px;font-size:56px;color:var(--ink)">GET IN <span class="accent">TOUCH</span></h2>
<div class="field" style="left:273px;top:3223px;width:315px;height:47px">Your Name</div>
<div class="field" style="left:612px;top:3223px;width:315px;height:47px">Subject</div>
<div class="field" style="left:273px;top:3296px;width:315px;height:47px">Email Address</div>
<div class="field" style="left:612px;top:3296px;width:315px;height:119px"></div>
<div class="field" style="left:273px;top:3368px;width:315px;height:47px">Phone</div>
<span class="btn-outline">LEARN MORE</span>

<!-- footer -->
<footer class="site-footer"></footer>
<span class="foot-brand-mark"></span>
<div class="foot-brand-name">RIDGELINE</div>
<div class="foot-brand-tag">Groundworks | Landscaping | Extensions</div>

<div class="foot-col">
  <h4 style="left:485px">CONTACT US</h4>
  <svg class="foot-icon" style="left:484px;top:3670px" viewBox="0 0 16 16"><path d="M8 1a5 5 0 0 0-5 5c0 4 5 9 5 9s5-5 5-9a5 5 0 0 0-5-5z" fill="#fff"/><circle cx="8" cy="6" r="2" fill="#1c2a48"/></svg>
  <span class="foot-link" style="left:508px;top:3668px;font-size:13.5px;line-height:17px">48 Oakfield Road, Suite 4<br>Austin 73301 TX</span>
  <svg class="foot-icon" style="left:484px;top:3722px" viewBox="0 0 16 16"><path d="M3 1l3 3-2 2c1 2 3 4 5 5l2-2 3 3-2 2C7 14 2 9 1 3z" fill="#fff"/></svg>
  <span class="foot-link" style="left:508px;top:3720px;font-size:15.5px">(555) 014 2290</span>
  <svg class="foot-icon" style="left:484px;top:3759px" viewBox="0 0 16 16"><rect x="1" y="3" width="14" height="10" fill="#fff"/><polyline points="1,3 8,9 15,3" fill="none" stroke="#1c2a48" stroke-width="1.3"/></svg>
  <span class="foot-link" style="left:508px;top:3756px;font-size:15.5px">hello@ridgelinebuild.com</span>
</div>
<div class="foot-col">
  <h4 style="left:777px">COMPANY</h4>
  <span class="foot-link" style="left:777px;top:3667px">Home</span>
  <span class="foot-link" style="left:777px;top:3694px">About Us</span>
  <span class="foot-link" style="left:777px;top:3721px">Projects</span>
  <span class="foot-link" style="left:777px;top:3748px">Services</span>
</div>
<div class="foot-col">
  <h4 style="left:957px">RESOURCES</h4>
  <span class="foot-link" style="left:957px;top:3667px">Testimonials</span>
  <span class="foot-link" style="left:957px;top:3694px">Sitemap</span>
  <span class="foot-link" style="left:957px;top:3721px">Cotact Us</span>
  <span class="foot-link" style="left:957px;top:3748px">Support</span>
</div>
<div class="footer-bar">© 2020 Ridgeline Construction. All Rights are Reserved.</div>

</body>
</html>
```